Travel Agency Website - Simple General

Need a 7 page simple design that is pretty repetitive. Need to be able to load quickly that is SEO optimized. Trying to give ideas on what they can do, be personal as we are local, but at the same time come across as professional and get information easily with little burden.

- Landing Page
- Brambleton Vacations Page
- Family Trips
- Road Trips from Texas
- Other Destinations
- About Us Page
- Contact Us Page

Target Market(s)

Families

Coding

Coded - Design and coding required

Number of Pages Required

5+ page

Colors

Designer to choose colors to be used in the design.

Requirements
Must have
• Like it to flow easily with our logo. Use that for colors, etc.

```html
<!DOCTYPE html>
<html lang="en">
<head>
<meta charset="UTF-8">
<title>Wayfarer Lane Travel Co. — Bucket List Worthy Trips</title>
<link rel="stylesheet" href="https://fonts.googleapis.com/css2?family=Playfair+Display:wght@700;800&family=Montserrat:wght@400;500;600;700&family=Allura&display=swap">
<style>
:root{
  --teal:#2e8a86;
  --teal-deep:#1f5c68;
  --gold:#c4944a;
  --ink:#1e1e1e;
  --white:#ffffff;
  --rule:#d9d9d9;
}
*{box-sizing:border-box;margin:0;padding:0}
html,body{width:797px;height:1200px;overflow:hidden;background:var(--white)}
body{font-family:"Montserrat",Arial,sans-serif;color:var(--ink);position:relative}
a{text-decoration:none}
.abs{position:absolute}

/* Hero */
.hero{position:absolute;left:0;top:0;width:797px;height:416px;overflow:hidden}
.hero-photo{position:absolute;inset:0;
  background:linear-gradient(100deg,#e9e4dc 0%,#d8cfc2 28%,#b7a58a 48%,#8a7a5e 62%,#c9c4bd 76%,#6c6a6e 100%)}
.hero-photo::after{content:"";position:absolute;inset:0;
  background:linear-gradient(180deg,rgba(90,90,110,.35) 0%,rgba(255,255,255,0) 35%,rgba(120,110,100,.2) 100%)}
.nav{position:absolute;left:35px;top:26px;width:726px;height:23px;background:var(--white);
  clip-path:polygon(12px 0,calc(100% - 12px) 0,100% 50%,calc(100% - 12px) 100%,12px 100%,0 50%)}
.nav a{position:absolute;top:0;line-height:23px;font-size:7px;font-weight:500;color:var(--ink);white-space:nowrap}
.brand-badge{position:absolute;left:352px;top:6px;width:94px;height:70px;background:var(--white);border-radius:14px;
  display:flex;flex-direction:column;align-items:center;justify-content:center;gap:3px}
.brand-badge .dot{width:8px;height:8px;border-radius:50%;background:var(--gold)}
.brand-name{font-family:"Playfair Display",Georgia,serif;font-weight:700;color:var(--teal-deep);font-size:11px;line-height:1.1;text-align:center}
.eyebrow{left:45px;top:133px;font-family:"Playfair Display",Georgia,serif;font-weight:700;font-size:16px;color:var(--gold);letter-spacing:.2px}
.script-title{left:36px;top:150px;font-family:"Allura",cursive;font-size:42px;color:var(--teal);white-space:nowrap;line-height:1.1}
.title-rule{left:35px;top:196px;width:333px;height:2px;background:var(--gold);border-radius:2px}
.hero-lede{left:35px;top:218px;width:275px;font-size:11.5px;line-height:16px;color:var(--ink)}
.btn-teal{left:40px;top:271px;width:230px;height:17px;background:var(--teal);color:var(--white);
  font-size:8.4px;font-weight:700;line-height:17px;text-align:center;letter-spacing:.2px;border-radius:2px}

/* Columns */
.section-title{position:absolute;left:0;width:797px;text-align:center;font-family:"Playfair Display",Georgia,serif;font-weight:800;font-size:29px;letter-spacing:.3px}
.choose-title{top:457px;color:var(--teal)}
.col{position:absolute;width:150px;text-align:center}
.icon-circle{width:52px;height:52px;border-radius:50%;margin:0 auto;display:flex;align-items:center;justify-content:center}
.icon-gold{background:var(--gold)}
.icon-white{background:#fbf8f3}
.col h3{font-family:"Playfair Display",Georgia,serif;font-weight:700;font-size:13px;line-height:15px;margin-top:9px;white-space:nowrap}
.col h3.long{font-size:11.5px}
.col p{font-size:7px;line-height:11px;margin:3px auto 0;width:140px}
.choose .col h3{color:var(--teal)}
.vrule{position:absolute;width:1px}
.choose .vrule{top:505px;height:108px;background:#e6e6e6}

/* Why */
.why{position:absolute;left:0;top:660px;width:797px;height:241px;
  background:linear-gradient(160deg,#235f6b 0%,#1f5a66 45%,#2a6773 70%,#1d5561 100%)}
.why-title{top:32px;color:var(--white)}
.why .col h3{color:var(--gold);text-transform:uppercase;margin-top:6px;line-height:14px}
.why .col p{color:var(--white)}
.why .vrule{top:82px;height:122px;background:rgba(255,255,255,.25)}

/* CTA */
.cta{position:absolute;left:0;top:901px;width:797px;height:166px;overflow:hidden;
  background:linear-gradient(180deg,#2f7fc8 0%,#5aa2d8 45%,#b9dbe8 68%,#7fd3d4 80%,#e9e6dc 100%)}
.cta-title{position:absolute;left:0;width:562px;top:29px;text-align:center;font-family:"Playfair Display",Georgia,serif;font-weight:700;font-size:29px;color:var(--white)}
.cta-sub{position:absolute;left:0;width:562px;top:70px;text-align:center;font-size:12px;line-height:17px;color:var(--white)}
.btn-gold{position:absolute;left:220px;top:110px;width:142px;height:17px;background:var(--gold);color:var(--white);
  font-size:8.4px;font-weight:700;line-height:17px;text-align:center;border-radius:2px}

/* Footer */
.footer{position:absolute;left:0;top:1067px;width:797px;height:133px}
.foot-badge{position:absolute;left:80px;top:36px;width:68px;height:54px;border-radius:12px;background:#f1f6f5;display:flex;align-items:center;justify-content:center}
.foot-badge .brand-name{font-size:9.5px}
.foot-tag{left:155px;top:44px;font-size:7.3px;line-height:11px;width:92px}
.foot-rule{position:absolute;width:1px;top:34px;height:57px;background:var(--rule)}
.foot-head{font-family:"Playfair Display",Georgia,serif;font-weight:700;color:var(--gold);font-size:9.5px;line-height:12px}
.foot-links{left:285px;top:33px;list-style:none}
.foot-links li{font-size:7.3px;line-height:10.2px}
.foot-links li.foot-head{font-size:9.5px;line-height:12px;margin-bottom:2px}
.contact{left:405px;top:33px;width:200px}
.contact-row{position:absolute;display:flex;align-items:center;gap:4px;white-space:nowrap}
.contact-ic{width:18px;height:18px;border-radius:50%;background:var(--gold);display:flex;align-items:center;justify-content:center;flex:none}
.contact-label{font-size:5.2px;font-weight:700;color:var(--gold);display:block}
.contact-value{font-size:7.2px;display:block}
.follow{left:636px;top:33px}
.socials{position:absolute;left:0;top:18px;display:flex;gap:10px}
.socials span{width:12px;height:12px;background:var(--ink);border-radius:2px;display:block}
.bottom-rule{position:absolute;left:80px;top:104px;width:638px;height:1px;background:var(--rule)}
.copyright{position:absolute;left:0;top:114px;width:797px;text-align:center;font-size:7px}
</style>
</head>
<body>

<header class="hero">
  <div class="hero-photo" role="img" aria-label="Photo: two travellers in a white convertible on a desert highway, one waving a sun hat, mountains behind"></div>
  <nav class="nav" aria-label="Main">
    <a href="#" style="left:17px">BRAMBLETON VACATIONS</a>
    <a href="#" style="left:130px">FAMILY TRIPS</a>
    <a href="#" style="left:207px">TEXAS ROAD TRIPS</a>
    <a href="#" style="left:440px">OUR OTHER DESTINATIONS</a>
    <a href="#" style="left:574px">ABOUT US</a>
    <a href="#" style="left:649px">CONTACT US</a>
  </nav>
  <div class="brand-badge">
    <span class="brand-name">Wayfarer Lane<br>Travel Co.</span>
    <span class="dot"></span>
  </div>
  <p class="abs eyebrow">CREATING MEMORIES.</p>
  <h1 class="abs script-title">Bucket List Worthy Trips</h1>
  <div class="abs title-rule"></div>
  <p class="abs hero-lede">Family vacations, magical getaways, and road trip adventures--planned with care by your local travel experts.</p>
  <a class="abs btn-teal" href="#">LET'S PLAN YOUR NEXT ADVENTURE</a>
</header>

<section class="choose">
  <h2 class="section-title choose-title">CHOOSE YOUR ADVENTURE</h2>
  <div class="vrule" style="left:221px"></div>
  <div class="vrule" style="left:399px"></div>
  <div class="vrule" style="left:576px"></div>

  <div class="col" style="left:57px;top:506px">
    <div class="icon-circle icon-gold">
      <svg width="28" height="28" viewBox="0 0 28 28" fill="none" stroke="#fff" stroke-width="1.3"><rect x="4" y="6" width="20" height="17" rx="2"/><path d="M4 11h20M9 4v4M19 4v4"/><path d="M8 20c3-4 9-4 12 0"/></svg>
    </div>
    <h3 class="long">BRAMBLETON VACATIONS</h3>
    <p>Experience the magic of Brambleton on land or at sea with customized itineraries for all ages.</p>
  </div>
  <div class="col" style="left:235px;top:506px">
    <div class="icon-circle icon-gold">
      <svg width="28" height="28" viewBox="0 0 28 28" fill="none" stroke="#fff" stroke-width="1.3"><circle cx="10" cy="9" r="3"/><circle cx="18" cy="9" r="3"/><path d="M5 23v-5a5 5 0 0 1 10 0v5M13 23v-5a5 5 0 0 1 10 0v5"/></svg>
    </div>
    <h3>Family Trips</h3>
    <p>Join our family on tried-and-tested adventures and let us tailor your perfect getaway.</p>
  </div>
  <div class="col" style="left:412px;top:506px">
    <div class="icon-circle icon-gold">
      <svg width="28" height="28" viewBox="0 0 28 28" fill="none" stroke="#fff" stroke-width="1.3"><path d="M17 4v20M17 7h6l2 2-2 2h-6M17 13h-6l-2 2 2 2h6"/><path d="M3 24h22"/><rect x="4" y="18" width="8" height="4" rx="1"/></svg>
    </div>
    <h3>Texas Road Trips</h3>
    <p>Discover incredible destinations close to home. We partner with Pinecrest Van Rentals for stress-free travel.</p>
  </div>
  <div class="col" style="left:590px;top:506px">
    <div class="icon-circle icon-gold">
      <svg width="28" height="28" viewBox="0 0 28 28" fill="none" stroke="#fff" stroke-width="1.3"><path d="M9 22s-5-5-5-9a5 5 0 0 1 10 0c0 4-5 9-5 9z"/><circle cx="9" cy="13" r="1.8"/><path d="M20 12s-3-3-3-6a3 3 0 0 1 6 0c0 3-3 6-3 6z"/><path d="M12 23h8a3 3 0 0 0 0-6" stroke-dasharray="2 2"/></svg>
    </div>
    <h3>Other Destinations</h3>
    <p>Whether you crave beaches, mountains, cities or a mix of everything, we'll help you get there.</p>
  </div>
</section>

<section class="why">
  <div class="abs" style="inset:0" role="img" aria-label="Faint photo: family with arms raised among tall forest trees"></div>
  <h2 class="section-title why-title">WHY TRAVEL WITH US?</h2>
  <div class="vrule" style="left:221px"></div>
  <div class="vrule" style="left:399px"></div>
  <div class="vrule" style="left:576px"></div>

  <div class="col" style="left:57px;top:82px">
    <div class="icon-circle icon-white">
      <svg width="28" height="28" viewBox="0 0 28 28" fill="none" stroke="#1f5c68" stroke-width="1.3"><circle cx="6" cy="7" r="2"/><circle cx="22" cy="7" r="2"/><circle cx="6" cy="21" r="2"/><circle cx="22" cy="21" r="2"/><path d="M8 7h12M20 7c4 0 4 7 0 7H8c-4 0-4 7 0 7h12"/></svg>
    </div>
    <h3>Personalized<br>Planning</h3>
    <p>Experience the magic of Brambleton on land or at sea with customized itineraries for all ages.</p>
  </div>
  <div class="col" style="left:235px;top:82px">
    <div class="icon-circle icon-white">
      <svg width="28" height="28" viewBox="0 0 28 28" fill="none" stroke="#1f5c68" stroke-width="1.3"><rect x="4" y="4" width="9" height="8" rx="1"/><circle cx="20" cy="9" r="3.5"/><path d="M14 24v-4a6 6 0 0 1 12 0v4"/><rect x="4" y="16" width="9" height="8" rx="1"/><path d="M7 16v-2h3v2"/></svg>
    </div>
    <h3>Expert<br>Guidance</h3>
    <p>Join our family on tried-and-tested adventures and let us tailor your perfect getaway.</p>
  </div>
  <div class="col" style="left:412px;top:82px">
    <div class="icon-circle icon-white">
      <svg width="28" height="28" viewBox="0 0 28 28" fill="none" stroke="#1f5c68" stroke-width="1.3"><circle cx="16" cy="10" r="6"/><path d="M16 7v3l2 2"/><path d="M3 20l4-2h6l4-2 5-2a1.5 1.5 0 0 1 1 3l-7 5H8l-3 2"/></svg>
    </div>
    <h3>Save Time<br>&amp; Stress</h3>
    <p>Discover incredible destinations close to home. We partner with Pinecrest Van Rentals for stress-free travel.</p>
  </div>
  <div class="col" style="left:590px;top:82px">
    <div class="icon-circle icon-white">
      <svg width="28" height="28" viewBox="0 0 28 28" fill="none" stroke="#1f5c68" stroke-width="1.3"><path d="M4 13h4v10H4zM8 14l4-6 1 1v4h5a2 2 0 0 1 0 4h-1a2 2 0 0 1 0 3h-1a2 2 0 0 1-1 3H8"/><path d="M18 4l6 2v9l-6 2-3-3V7z"/><circle cx="20" cy="10" r="2"/></svg>
    </div>
    <h3>Best<br>Value</h3>
    <p>Whether you crave beaches, mountains, cities or a mix of everything, we'll help you get there.</p>
  </div>
</section>

<section class="cta">
  <div class="abs" style="left:560px;top:0;width:237px;height:166px;background:linear-gradient(180deg,rgba(255,255,255,.15),rgba(230,225,215,.35))" role="img" aria-label="Photo: family of four in white summer clothes walking on a tropical beach"></div>
  <h2 class="cta-title">Let's Plan Something Amazing!</h2>
  <p class="cta-sub">Whether it's a weekend getaway or the trip of a lifetime,<br>we're here to make it unforgettable.</p>
  <a class="btn-gold" href="#">GET STARTED TODAY</a>
</section>

<footer class="footer">
  <div class="foot-badge"><span class="brand-name">Wayfarer Lane<br>Travel Co.</span></div>
  <p class="abs foot-tag">Your local travel partner for memories that last a lifetime.</p>
  <div class="foot-rule" style="left:261px"></div>
  <ul class="abs foot-links">
    <li class="foot-head">Quick Links</li>
    <li>Brambleton Vacations</li>
    <li>Family Trips</li>
    <li>Texas Road Trips</li>
    <li>Other Destinations</li>
  </ul>
  <div class="foot-rule" style="left:381px"></div>
  <div class="abs contact">
    <p class="foot-head">Quick Links</p>
    <div class="contact-row" style="left:0;top:17px">
      <span class="contact-ic"><svg width="10" height="10" viewBox="0 0 10 10" fill="none" stroke="#fff" stroke-width="1"><rect x="1" y="2" width="8" height="6"/><path d="M1 2l4 3 4-3"/></svg></span>
      <span><span class="contact-label">Our Email:</span><span class="contact-value">hello@wayfarerlanetravel.com</span></span>
    </div>
    <div class="contact-row" style="left:0;top:40px">
      <span class="contact-ic"><svg width="10" height="10" viewBox="0 0 10 10" fill="none" stroke="#fff" stroke-width="1"><path d="M5 9S2 6 2 4a3 3 0 0 1 6 0c0 2-3 5-3 5z"/><circle cx="5" cy="4" r="1"/></svg></span>
      <span><span class="contact-label">Our Address:</span><span class="contact-value">Maple Hollow, TX 77000</span></span>
    </div>
    <div class="contact-row" style="left:122px;top:40px">
      <span class="contact-ic"><svg width="10" height="10" viewBox="0 0 10 10" fill="none" stroke="#fff" stroke-width="1"><rect x="3" y="1" width="4" height="8" rx="1"/><path d="M4.5 7.5h1"/></svg></span>
      <span><span class="contact-label">PHONE:</span><span class="contact-value">555-010-0199</span></span>
    </div>
  </div>
  <div class="foot-rule" style="left:611px"></div>
  <div class="abs follow">
    <p class="foot-head">Follow Us</p>
    <div class="socials" aria-label="Social links"><span></span><span></span><span></span><span></span></div>
  </div>
  <div class="bottom-rule"></div>
  <p class="copyright">© 2026 Wayfarer Lane Travel Co. All rights reserved.</p>
</footer>

</body>
</html>
```